Tumbler Cafe - Menu Redesign

What We Want

We're looking for a bold redesign of our current menu. Our current menu is tired and boring and does not accurately reflect our revitalization of the Tumbler Cafe brand. Attachments will be submitted with the campaign for menu items.

Design Guidelines

• Creative use of typography and color. Think Bold, Fun, Loud and uninhibited.
• Fluid, easy to read, layout that emphasizes readability.
• The subtle, demure, look of typographic columns (examples below in resources)
• Creative use of 'wells' for menu item highlights as well as great boarders
• Loud typefaces as long as readability is the focus & emphasis.
• Small illustrations/icons but they must not effect or take the focus from the readability of the menu
• Big, oversized, menu that will look great on recycled paper
• Subtle watermarks/illustrations
• creative use of textures / highlights / section breaks

Menu Requirements

• 9”x12” paper size. Please notify us if your design works better in a different format.
• Oversized, designed for printing on recycled paper.
• Single Page Menu (use lunch on front and breakfast on back)
• Do not use $ or "..." in pricing. Please space all prices equally.
• Simplistic layout that emphasizes readability and logical navigation of menu items.
• Acceptable file types
• Photoshop
• Indesign
• illustrator
• Please contact us before you submit a design if you plan on using something else
• HTML/CSS would be a huge benefit. It's not a must, but it will definitely help you win the award.
• Must retain some of our current color scheme (red/orange/yellow – see attachments/website).

NOTE: Please download ALL attached resources for the project.
Updates

Current web site:  www.tumblercafe-example.com

please read attachment:  tumbler_menu_redesign_request.docx

Lots of good information & examples on menus we like and the design elements featured in the menu.

All,

Thanks for your design submissions!  With all the designs that have be submitted so far, we are confident that our money will be well spent.  I have changed the project to non-refundable.  Please continue working on your designs using the design_request doc that's posted for guidelines/requirements.  I will provide specific feedback to designs as needed.

For your convenience:

Design Guidelines

 

Creativeuse of typography and color.  Think Bold,Fun, Loud and uninhibited.

Fluid,easy to read, layout that emphasizes readability.

Thesubtle, demure, look of typographic columns (examples below in resources)

Creativeuse of 'wells' for menu item highlights as well as great boarders

Loudtypefaces as long as readability is the focus & emphasis.

Smallillustrations/icons but they must not effect or take the focus from thereadability of the menu

Big,oversized, menu that will look great on recycled paper

Subtlewatermarks/illustrations

creativeuse of textures / highlights / section breaks

 

  MenuRequirements

 

9”x12”paper size.  Please notify us if yourdesign works better in a different format.

Oversized,designed for printing on recycled paper.

SinglePage Menu (use lunch on front and breakfast on back)

Donot use $ or "..." in pricing.Please space all prices equally.

Simplisticlayout that emphasizes readability and logical navigation of menu items.

Acceptablefile types

Photoshop

Indesign

illustrator 

Pleasecontact us before you submit a design if you plan on using something else

HTML/CSSwould be a huge benefit.  It's not amust, but it will definitely help you win the award.

Mustretain some of our current color scheme (red/orange/yellow – seeattachments/website). 

 

Do Not Use

 

Skeuomorphismin any way.

Wedo not want any actual pictures of food on the menu (subtle illustrations /icons are great and encouraged).

Typefacesthat are hard to read.

Thanks!

dana

Reason: need to incorporate changes to menu / menu items

Please expect some new copy tonight (USA EST) for the breakfast menu items.  Thanks!

dana

COPY UPDATE:  Please check new menu item listing (revision 3) for updated copy.  Please revisit all menu items as I have grouped, consolidated, and eliminated some items.

Thanks!

dana 

DESIGN UPDATE:  I added an omelette hero/jumbotron design that we'd like to use to display the omelettes on the breakfast menu.  It doesn't have to be exactly like this one, it's just meant to be a guideline.  Please take a look and see if you can fit it in to your design.  Also, the copy has been updated for the breakfast & lunch menus.

Reason: Revised design changes not yet received.

Reason: Designer needs more tine to complete final submission. This will be the last extension. Thanks! dana

Target Market(s)

Women - 60% or more. Mostly professionals. 18-55.
Men - Professionals mostly. Judges, Attorneys, Agents, Ect. Ages 18-55.

Industry/Entity Type

Printing

Colors
f37022
ec1f27
f78f20
faa54b
f04a50
fee18a
faee3e

Requirements
Must have
• see menu requirements in task description.
Nice to have
• Design Ideas We Love

http://www.menugallery-example.com/menucraft/archives/stonegate_inn.php
We like: typefaces, typographic columns & layout, use of butcher-block print, simplicity
We don't like: lack of bold, color lack of textures, lack of general vitality in the brand, no use of icons/illustrations

http://www.menugallery-example.com/menucraft/archives/patty_vault.php
We like: typefaces, bold headers & section breaks, texturized typefaces, use of illustrations, and specifically we love how they did the 'custom creation' menu
We don't like: lack of bold color, lack of subtle texturing, little more use of illustrated icons would be nice

http://www.menugallery-example.com/menucraft/archives/the_rowdy_roost.php
We like: use of bold colors, organization & layout, the section highlights are nice
We don't like: lack of textures, lack subtle illustrations/icons.

http://www.menugallery-example.com/menucraft/archives/wexford_mill.php
We like: use of textures, typefaces, layout & organization, single page menu
We don't like: lack of textures, lack of bold color, lack of icons and menu item hightlights

http://www.menugallery-example.com/menucraft/archives/zibbo_caf.php
We like: use of texturing, typesfaces, layout & organization, creative use of illustrations/icons, bold colors
We don't like: not a huge fan of the bordering; and illustrations take up too much room for single page menu

http://www.menugallery-example.com/menucraft/archives/ved_hjornet_af_torvet.php
We like: creative use of typefaces, organization & layout, cool illustrations, oversized menu, section seperators are cool & unique
We don't like: lack of textures, menu items inside illustrations, typefaces can get hard to read in certain areas
Should not have
• Do Not Use

• Skeuomorphism in any way.
• We do not want any actual pictures of food on the menu (subtle illustrations / icons are great and encouraged).
• Typefaces that are hard to read.

```html
<!DOCTYPE html>
<html lang="en">
<head>
<meta charset="utf-8">
<title>Tumbler Cafe Breakfast Menu</title>
<link rel="stylesheet" href="https://fonts.googleapis.com/css2?family=Nunito:wght@900&family=Arimo:wght@400;700&display=swap">
<style>
:root{
  --paper:#f9c85c;
  --paper-light:#fcd97a;
  --band:#c12f60;
  --band-edge:#a8254f;
  --band-light:#e0719a;
  --item:#e3211f;
  --desc:#e0452a;
  --ink:#111;
  --white:#fff;
}
*{box-sizing:border-box;margin:0;padding:0}
html,body{width:735px;height:1200px;overflow:hidden}
body{font-family:"Arimo",Arial,sans-serif;background:linear-gradient(180deg,var(--paper-light),var(--paper) 40%,var(--paper));position:relative;color:var(--item)}
.section-band{position:absolute;left:0;width:735px;height:58px;
  background:linear-gradient(90deg,var(--band) 0,var(--band) 88%,var(--band-light) 88%,var(--band-light) 100%);
  border-top:3px solid var(--band-edge);border-bottom:3px solid var(--band-edge)}
.section-band h2{font-family:"Nunito",sans-serif;font-weight:900;color:var(--white);font-size:36px;line-height:52px;padding-left:14px}
.band-short{width:480px;background:var(--band)}
.brand-box{position:absolute;left:486px;top:20px;width:238px;height:160px;background:var(--white);border:2px solid var(--ink);text-align:center;color:var(--ink);padding-top:18px}
.brand-name{font-family:"Arimo",sans-serif;font-weight:700;font-size:30px;line-height:36px}
.brand-sub{font-size:22px;line-height:30px;margin-top:2px}
.brand-hours{font-size:12px;line-height:15px;margin-top:6px}
.list{position:absolute;font-size:13.5px;line-height:16.5px}
.row{display:flex;justify-content:space-between}
.row .price{white-space:nowrap}
.desc{font-size:11px;line-height:13px;color:var(--desc)}
.center{text-align:center}
</style>
</head>
<body>

<div class="section-band band-short" style="top:0"><h2>Sides</h2></div>
<div class="brand-box">
  <div class="brand-name">Tumbler Cafe</div>
  <div class="brand-sub">Breakfast</div>
  <div class="brand-hours">Served 7am to 11:30 am M-F<br>8:00am to 12:00pm Saturday<br>and 8:00am to 1:00 on Sunday</div>
</div>

<div class="list" style="top:84px;left:14px;width:440px">
  <div class="row"><span style="width:330px">Tusk &amp; Oak Bacon, Hollowell's Turkey Bacon, Sausage, Turkey Sausage, Canadian Roll or Ham Slice</span><span class="price" style="align-self:flex-end">2.75</span></div>
  <div class="row"><span>Side of Home fries</span><span class="price">2.00</span></div>
  <div class="row"><span>Side of Eggs</span><span class="price">2.50</span></div>
  <div class="row"><span>Big English Muffin</span><span class="price">1.25</span></div>
  <div class="row"><span>Toast</span><span class="price">1.25</span></div>
  <div class="row"><span>Grilled Yogurt Muffin</span><span class="price">1.75</span></div>
  <div class="row"><span>Toasted Bagel</span><span class="price">1.50</span></div>
  <div class="row"><span>Toasted Bagel with cream cheese</span><span class="price">2.00</span></div>
</div>
<div class="list" style="top:300px;left:14px;width:710px">
  <div class="row"><span style="width:400px">Meadowmill Oatmeal with brown sugar and milk</span><span class="price" style="width:126px">3.00</span><span style="width:110px">with raisins 3.50</span><span style="margin-left:auto">with fruit 4.50</span></div>
  <div class="row" style="width:440px"><span>Quinoa with raisins and fruit</span><span class="price">5.00</span></div>
</div>

<div class="section-band" style="top:348px"><h2>Omeletes</h2></div>
<div class="list" style="top:418px;left:14px;width:705px">
  <div class="row"><span>Cheese Omelet with Taters and toast</span><span class="price">6.50</span></div>
  <div class="row"><span>Hunters Omelet: <span class="desc">Bacon, Potato, Onions and Cheddar Omelet w/ taters &amp; toast</span></span><span class="price">8.95</span></div>
  <div class="row"><span>Fruity French Ile Omelet: <span class="desc">Ham, Brie &amp; Raspberry Jam Omelet w/ taters &amp; toast</span></span><span class="price">8.95</span></div>
  <div class="row"><span>Western Omelet: <span class="desc">Ham, Cheddar, pepper and onion Omelet w/ taters &amp; toast</span></span><span class="price">8.95</span></div>
  <div class="row"><span>South West White Veggie Omelet</span><span class="price">10.95</span></div>
  <div class="desc" style="padding-left:30px;width:520px">Four egg whites with Monterey Jack cheese, Tomatoes, Onions, peppers, Spinach and our home made salsa served with sliced tomatoes and toast</div>
</div>

<div class="section-band" style="top:578px"><h2>Eggs</h2></div>
<div class="list" style="top:644px;left:14px;width:260px">
  <div class="row"><span>Eggs, Taters and Toast</span><span class="price">5.50</span></div>
  <div class="row"><span>Egg Sandwich</span><span class="price">2.50</span></div>
  <div class="row"><span>Egg and Cheese Sandwich</span><span class="price">3.00</span></div>
  <div class="row"><span>Meat, Egg, and Cheese Sandwich</span><span class="price">4.75</span></div>
  <div class="row"><span>Egg, Cheese and Veggie Sandwich</span><span class="price">4.75</span></div>
</div>
<div class="list" style="top:644px;left:450px;width:270px">
  <div class="row"><span>Egg Whites Add</span><span class="price">1.50</span></div>
  <div class="row"><span>Two-egg Sandwich</span><span class="price">3.50</span></div>
  <div class="row"><span>Two-egg and Cheese Sandwich</span><span class="price">4.00</span></div>
  <div class="row"><span>in a bagel or wrap</span><span class="price">Add .50</span></div>
</div>
<div class="list desc center" style="top:760px;left:0;width:735px">
  <div>Add Veggies: mushrooms, tomatoes, onion, broccoli, spinach, peppers, jalapenos</div>
  <div>Add .50 each &nbsp;&nbsp;&nbsp;&nbsp; Egg whites: Add 1.50</div>
</div>

<div class="section-band" style="top:824px"><h2>Pancakes &amp; French Toast</h2></div>
<div class="list" style="top:892px;left:14px;width:300px">
  <div class="row"><span>Buttermilk Pancakes (3)</span><span class="price">5.25</span></div>
  <div class="row"><span>French Toast (3)</span><span class="price">5.50</span></div>
</div>
<div class="list" style="top:892px;left:410px;width:310px">
  <div class="row"><span>Short Stack Buttermilk Pancakes (2)</span><span class="price">4.25</span></div>
  <div class="row"><span>Short Stack French Toast (2)</span><span class="price">4.25</span></div>
</div>
<div class="list center" style="top:936px;left:0;width:735px">Upgrade to 100 % Maple Syrup &nbsp;1.50</div>

<div class="section-band" style="top:972px"><h2>Tumbler Favorites</h2></div>
<div class="list" style="top:1040px;left:14px;width:705px">
  <div class="row"><span>Hasta La Pasta</span><span class="price">7.95</span></div>
  <div class="desc" style="padding-left:14px;width:560px">Scrambled eggs in a tortilla topped with melted cheese and our home made salsa served w/ home fries</div>
  <div class="row" style="margin-top:4px"><span>Glutton's Paradise</span><span class="price">8.95</span></div>
  <div class="desc" style="padding-left:14px">3 eggs your way, 2 pancakes and a byproduct of your choice</div>
  <div class="row" style="margin-top:4px"><span>Breakfast Burrito</span><span class="price">5.95</span></div>
  <div class="desc" style="padding-left:14px;width:560px">Large Flour Tortilla filled with Scrambled Eggs, bacon, black beans, Home fries, cheddar cheese, and our home made salsa</div>
</div>

</body>
</html>
```